Larkspur Dental Centre Buderim Opening special DL flyer

dl flyer design with opening special offers and services provide and the location we are in

opening special offer : exam, clean and flouride treatment for $129 or No Gap if with Health Insurance.
$99 mouth guards for footy season
Emergency Dental Appointments Available everyday!!!
Open on Saturdays

Services:
6 monthly Maintainence
CAD/CAM Dentistry
Conscious Sedation
Cosmetic Dentistry
Crowns and Bridges
Dental Implant
Fissure Sealants
Duravex
Periodontal Treatment
Root Canal Treatment
Teeth Whitening
Tooth Coloured Fillings
Tooth Replacement

Interest Free Payment Plans Available

Address: Larkspur Dental Centre Buderim
318D, Kellet Road, Buderim - 4556
Ph: 07-5481 2936
email: admin@larkspurdentalcentrebuderim.com.au
Website: www.larkspurdentalcentrebuderim.com.au

Opening Hours:
Mon/Wed 8:30AM - 5PM
Thursday 9AM - 7PM
Friday 9AM - 5PM
Saturday 9AM - 1PM

Target Market(s)

local community

Industry/Entity Type

Dental

Font styles to use
Serif

Requirements
Must have
• all the above details

```html
<!DOCTYPE html>
<html lang="en">
<head>
<meta charset="utf-8">
<title>Larkspur Dental Centre Buderim – Opening Special</title>
<link href="https://fonts.googleapis.com/css2?family=Crimson+Pro:wght@400;500;600;700&display=swap" rel="stylesheet">
<style>
  :root {
    --ink: #231f20;
    --dark: #262223;
    --white: #ffffff;
    --accent: #8fb86a;
    --text: #2a2627;
  }
  * { margin: 0; padding: 0; box-sizing: border-box; }
  html, body { width: 849px; height: 1200px; overflow: hidden; background: var(--white); }
  .flyer {
    position: relative; width: 849px; height: 1200px; overflow: hidden;
    font-family: "Crimson Pro", Georgia, serif; color: var(--text);
    background: var(--white);
  }
  .header {
    position: absolute; left: 0; top: 0; width: 849px; height: 134px;
    background: var(--dark);
  }
  .brand {
    position: absolute; left: 36px; top: 46px;
    display: flex; align-items: center; gap: 10px;
  }
  .brand-dot {
    width: 34px; height: 34px; border-radius: 50%;
    background: var(--accent);
  }
  .brand-name {
    color: var(--white); font-size: 20px; font-weight: 500;
    letter-spacing: 0.8px; line-height: 1.1; text-transform: uppercase;
  }
  .header-address {
    position: absolute; left: 602px; top: 34px;
    color: var(--white); font-size: 16px; line-height: 20.5px;
    letter-spacing: 0.8px; font-style: normal;
  }
  .hero {
    position: absolute; left: 0; top: 134px; width: 849px; height: 547px;
    background:
      linear-gradient(180deg, rgba(0,0,0,0) 55%, rgba(40,25,25,0.55) 100%),
      radial-gradient(ellipse 260px 180px at 360px 300px, #c9a48c 0%, rgba(201,164,140,0) 100%),
      radial-gradient(ellipse 300px 300px at 760px 420px, #d8d6d4 0%, rgba(216,214,212,0) 100%),
      radial-gradient(ellipse 200px 360px at 40px 300px, #8a3f3a 0%, rgba(138,63,58,0) 100%),
      linear-gradient(90deg, #8e4a42 0%, #b8a896 35%, #cfc9bd 60%, #bfb8b0 100%);
  }
  .offer {
    position: absolute; left: 58px; top: 542px; width: 760px;
    color: var(--white); font-size: 23px; line-height: 30.7px; letter-spacing: 1.2px;
  }
  .offer-main { font-weight: 700; }
  .services-title, .hours-title {
    position: absolute; left: 0; width: 849px; text-align: center;
    font-size: 16px; font-weight: 700; letter-spacing: 1px; color: var(--ink);
  }
  .services-title { top: 702px; }
  .service-list {
    position: absolute; list-style: none;
    font-size: 15.5px; line-height: 20.6px; letter-spacing: 1px;
  }
  .service-list.left { left: 130px; top: 731px; }
  .service-list.right { right: 131px; top: 729px; text-align: right; }
  .hours-title { top: 886px; }
  .hours {
    position: absolute; left: 0; top: 915px; width: 849px; text-align: center;
    list-style: none; font-size: 15.5px; line-height: 20.6px; letter-spacing: 1px;
  }
  .payment-note {
    position: absolute; left: 0; top: 1008px; width: 849px; text-align: center;
    font-size: 16px; font-weight: 600; letter-spacing: 1px; color: var(--ink);
  }
  .saturday-note {
    position: absolute; left: 0; top: 1044px; width: 849px; text-align: center;
    font-size: 23px; font-weight: 700; letter-spacing: 1.5px; color: var(--ink);
  }
  .footer-band { position: absolute; left: 0; top: 1100px; width: 849px; height: 100px; }
  .contact {
    position: absolute; left: 0; top: 1118px; width: 849px; text-align: center;
    color: var(--white); font-size: 16px; line-height: 20.6px; letter-spacing: 1px;
    font-style: normal;
  }
</style>
</head>
<body>
<main class="flyer">
  <header class="header">
    <div class="brand">
      <span class="brand-dot"></span>
      <span class="brand-name">Larkspur Dental<br>Centre</span>
    </div>
    <address class="header-address">
      Larkspur Dental Centre,<br>
      Buderim 318D,<br>
      Kellet Road, Buderim - 4556
    </address>
  </header>

  <section class="hero" role="img" aria-label="Photo of a dentist in gloves examining a young patient's teeth in the dental chair"></section>

  <div class="offer">
    <p class="offer-main">Exam, Clean and Flouride Treatment for $129 or No Gap if with Health Insurance.</p>
    <p>*$99 mouth guards for footy season.</p>
    <p>*Emergency Dental Appointments Available everyday!!!</p>
  </div>

  <h2 class="services-title">Services</h2>
  <ul class="service-list left">
    <li>6 Months Maintenence</li>
    <li>CAD/CAM Dentistry</li>
    <li>Conscious Sedation</li>
    <li>Cosmetic Dentistry</li>
    <li>Crowns and Bridges</li>
    <li>Dental Implant</li>
    <li>Fissure Sealants</li>
  </ul>
  <ul class="service-list right">
    <li>Duravex</li>
    <li>Periodontal Treatment</li>
    <li>Root Canal Treatment</li>
    <li>Teeth Whitening</li>
    <li>Tooth Coloured Fillings</li>
    <li>Tooth Replacement</li>
  </ul>

  <h2 class="hours-title">Opening Hours</h2>
  <ul class="hours">
    <li>Mon/Wed 8:30AM - 5PM</li>
    <li>Thursday 9AM - 7PM</li>
    <li>Friday 9AM - 5PM</li>
    <li>Saturday 9AM - 1PM</li>
  </ul>

  <p class="payment-note">Interest Free Payment Plans Available</p>
  <p class="saturday-note">Open on Saturdays</p>

  <svg class="footer-band" viewBox="0 0 849 100" aria-hidden="true">
    <path d="M0 32 Q424.5 -12 849 32 L849 100 L0 100 Z" fill="var(--dark)"/>
  </svg>
  <address class="contact">
    Phone: 07-5481 2936<br>
    email: admin@larkspurdentalcentrebuderim.com.au<br>
    www.larkspurdentalcentrebuderim.com.au
  </address>
</main>
</body>
</html>
```